Ecommerce Web Design Platform "Vela Glow Society"

Want the website to Mimic
www.penytrimguild.example but with a more beautiful colored layout.
Also
www.maplecrate.example is another similar type website. Once they get through the initial page then they need to pick their style hair.
The front landing page:
It must have 3 tiers on the first page for customer to choose from:
1. Free Membership: Includes a Silver Vela Glow Society Membership, 10% off all products, Video Tutorials, and Coupons
2. $4.99 a month: Includes a Gold Vela Glow Society Membership, An initial free $25.00 hair product of your choice! 15 % off all products, Video Tutorials, Weekly Flash Sales and Coupons
$49.00 subscription: Includes 30% off all products, Video Tutorials, Weekly Flash
Sales and Coupons
Page 2
If they pick the hair tier it goes into another page; the next page they need to pick the type of hair they have
1. Straight
2. Wavy
Page 3
The third page they need to pick the color of hair. (photos attached)
Page 4
They need to pick the type of wavy hair if they choose wavy. (working on photos)
Updates
Target Market(s)
Women
Industry/Entity Type
Hair And Beauty
Look and feel

```html
<!DOCTYPE html>
<html lang="en">
<head>
<meta charset="utf-8">
<title>Vela Glow Society</title>
<link href="https://fonts.googleapis.com/css2?family=Roboto:wght@300;400;500;700&display=swap" rel="stylesheet">
<style>
:root{
  --pink:#e0408f;
  --pink-deep:#a3155f;
  --pink-soft:#f06ab0;
  --ink:#222;
  --text:#444;
  --muted:#777;
  --card-bg:#f4f4f4;
  --card-line:#ddd;
  --footer:#2b2b2b;
  --footer-text:#aaa;
  --white:#fff;
}
*{box-sizing:border-box;margin:0;padding:0}
html,body{width:1200px;height:2190px;overflow:hidden}
body{font-family:'Roboto',sans-serif;color:var(--text);background:var(--white);position:relative}
ul{list-style:none}

/* Hero */
.hero{position:absolute;left:0;top:0;width:1200px;height:628px;
  background:radial-gradient(circle at 62% 45%,#f4a6d0 0,#d64a97 32%,var(--pink-deep) 75%);overflow:hidden}
.hero-photo{position:absolute;left:490px;top:150px;width:710px;height:478px;
  background:radial-gradient(ellipse at 50% 40%,#d9b39a 0,#b78564 40%,rgba(150,60,90,.0) 75%)}
.brand{position:absolute;left:545px;top:29px;width:111px;height:111px;border-radius:12px;background:#111;
  display:flex;align-items:center;justify-content:center;text-align:center;box-shadow:0 4px 10px rgba(0,0,0,.3)}
.brand span{color:var(--white);font-weight:500;font-size:15px;line-height:1.2;letter-spacing:1px}
.menu{position:absolute;left:1029px;top:74px;display:flex;align-items:center;gap:14px;color:var(--white);font-size:13px;font-weight:500}
.hero-title{position:absolute;left:74px;top:230px;color:var(--white);font-size:44px;font-weight:700;line-height:52px}
.hero-sub{position:absolute;left:75px;top:346px;color:var(--white);font-size:26px;font-weight:400}
.hero-btn{position:absolute;left:75px;top:411px;width:197px;height:45px;border-radius:23px;background:var(--pink);
  color:var(--white);font-size:18px;font-weight:500;display:flex;align-items:center;justify-content:center}
.hero-arrows{position:absolute;left:74px;top:544px}

/* Plans */
.plan{position:absolute;top:673px;width:332px;height:431px;background:var(--card-bg);border:1px solid var(--card-line)}
.plan-head{height:66px;background:var(--pink);color:var(--white);display:flex;align-items:center;justify-content:center;font-size:24px;font-weight:400;letter-spacing:.5px}
.plan-head b{font-size:32px;font-weight:500;margin-right:8px}
.plan-list{display:flex;flex-direction:column;justify-content:space-around;height:355px;padding:4px 14px 6px}
.plan-item{display:flex;align-items:center;gap:18px;font-size:15px;font-weight:500;color:var(--ink);line-height:19px}
.plan-item em{font-style:normal;color:var(--pink)}
.ico{flex:none;width:50px;height:50px;border-radius:50%;border:2px solid var(--pink);background:var(--white);display:flex;align-items:center;justify-content:center}

/* Products */
.products{position:absolute;left:0;top:1153px;width:1200px;height:439px;
  background:radial-gradient(ellipse at 50% 50%,#f27cb9 0,var(--pink) 60%)}
.products h2{position:absolute;left:0;top:36px;width:1200px;text-align:center;color:var(--white);font-size:42px;font-weight:700}
.products-intro{position:absolute;left:0;top:97px;width:1200px;text-align:center;color:var(--white);font-size:12px}
.cat{position:absolute;top:135px;width:200px}
.cat-photo{width:131px;height:131px;border-radius:50%;border:5px solid rgba(255,255,255,.35);margin-bottom:20px}
.cat h3{color:var(--white);font-size:15px;font-weight:400;margin-bottom:6px}
.cat li{color:var(--white);font-size:12px;line-height:22px}
.cat li::before{content:"›";margin-right:9px}

/* Media */
.section-title{position:absolute;top:1625px;color:var(--pink);font-size:27px;font-weight:500}
.video{position:absolute;left:74px;top:1686px;width:420px;height:310px;background:linear-gradient(135deg,#8a7a72,#4a3a34 60%,#6c6864)}
.video svg{position:absolute;left:182px;top:127px}
.post{position:absolute;left:527px;width:600px;height:140px}
.post-photo{position:absolute;left:0;top:0;width:194px;height:140px}
.post-body{position:absolute;left:210px;top:0;width:390px}
.post h4{color:var(--pink);font-size:19px;font-weight:400;margin-top:1px}
.post time{display:block;font-size:13px;color:var(--ink);margin:14px 0 6px}
.post p{font-size:11px;line-height:25px;color:var(--muted)}

/* Footer */
.footer{position:absolute;left:0;top:2040px;width:1200px;height:150px;background:var(--footer)}
.foot-brand{position:absolute;left:74px;top:44px;width:62px;height:62px;border-radius:8px;background:#111;border:2px solid #444;
  display:flex;align-items:center;justify-content:center;text-align:center;color:var(--white);font-size:8px;font-weight:500;line-height:1.2}
.foot-copy{position:absolute;left:157px;top:56px;color:#888;font-size:11px;line-height:20px}
.foot-col{position:absolute;top:38px}
.foot-col li{color:var(--footer-text);font-size:11px;line-height:27px;letter-spacing:.3px}
.social{position:absolute;left:947px;top:67px;display:flex;gap:17px}
.social span{width:14px;height:14px;border-radius:50%;background:#ccc}
</style>
</head>
<body>

<header class="hero">
  <div class="hero-photo" role="img" aria-label="Photo of three smiling women with long flowing hair"></div>
  <div class="brand"><span>VELA GLOW<br>SOCIETY</span></div>
  <div class="menu">MEANU
    <svg width="28" height="24" viewBox="0 0 28 24"><rect y="1" width="28" height="4" fill="#fff"/><rect y="10" width="28" height="4" fill="#fff"/><rect y="19" width="28" height="4" fill="#fff"/></svg>
  </div>
  <h1 class="hero-title">WELCOME TO VELA<br>GLOW SOCIETY.</h1>
  <p class="hero-sub">Sed ut perspiciatis unde omnis</p>
  <a class="hero-btn">LEARN MORE</a>
  <svg class="hero-arrows" width="52" height="26" viewBox="0 0 52 26"><path d="M14 3 L4 13 L14 23" stroke="#fff" stroke-width="4" fill="none"/><path d="M38 3 L48 13 L38 23" stroke="#fff" stroke-width="4" fill="none"/></svg>
</header>

<section class="plans">
  <div class="plan" style="left:76px">
    <div class="plan-head">FREE MEMBERSHIP</div>
    <ul class="plan-list">
      <li class="plan-item"><span class="ico"><svg width="22" height="26" viewBox="0 0 22 26"><circle cx="11" cy="9" r="7" fill="none" stroke="#888" stroke-width="2"/><path d="M6 14 L4 24 L9 21 L11 24 M16 14 L18 24 L13 21 L11 24" fill="none" stroke="#888" stroke-width="2"/></svg></span>Includes a Silver Vela Glow Society Membership</li>
      <li class="plan-item"><span class="ico"><svg width="20" height="24" viewBox="0 0 20 24"><text x="10" y="19" text-anchor="middle" font-family="Roboto,sans-serif" font-size="20" font-weight="500" fill="#222">$</text></svg></span><span><em>10% Off</em> All Products</span></li>
      <li class="plan-item"><span class="ico"><svg width="22" height="16" viewBox="0 0 22 16"><rect width="22" height="16" rx="4" fill="#222"/><path d="M9 4 L15 8 L9 12Z" fill="#fff"/></svg></span>Video Tutorials</li>
      <li class="plan-item"><span class="ico"><svg width="22" height="22" viewBox="0 0 22 22"><path d="M3 12 L12 3 L19 3 L19 10 L10 19Z" fill="#222"/><circle cx="15.5" cy="6.5" r="1.6" fill="#fff"/><path d="M8 11 L11 14 M10 9 L13 12" stroke="#fff" stroke-width="1.2"/></svg></span>Coupons</li>
    </ul>
  </div>

  <div class="plan" style="left:435px">
    <div class="plan-head"><b>$4.99</b>a month</div>
    <ul class="plan-list">
      <li class="plan-item"><span class="ico"><svg width="22" height="26" viewBox="0 0 22 26"><circle cx="11" cy="9" r="7" fill="#e0b62a"/><path d="M6 14 L4 24 L9 21 L11 24 M16 14 L18 24 L13 21 L11 24" fill="none" stroke="#c39a1a" stroke-width="2"/></svg></span>Includes a Gold Vela Glow Society Membership</li>
      <li class="plan-item"><span class="ico"><svg width="20" height="24" viewBox="0 0 20 24"><text x="10" y="19" text-anchor="middle" font-family="Roboto,sans-serif" font-size="20" font-weight="500" fill="#222">$</text></svg></span><span>An initial <em>FREE $25.00</em> Hair Product of your Choice! <em>15 %</em> off All Products</span></li>
      <li class="plan-item"><span class="ico"><svg width="22" height="16" viewBox="0 0 22 16"><rect width="22" height="16" rx="4" fill="#222"/><path d="M9 4 L15 8 L9 12Z" fill="#fff"/></svg></span>Video Tutorials</li>
      <li class="plan-item"><span class="ico"><svg width="20" height="20" viewBox="0 0 20 20"><rect x="1" y="3" width="18" height="16" rx="2" fill="none" stroke="#222" stroke-width="2"/><path d="M1 8 H19 M6 1 V5 M14 1 V5 M7 8 V19 M13 8 V19 M1 13.5 H19" stroke="#222" stroke-width="1.5"/></svg></span>Weekly Flash Sales</li>
      <li class="plan-item"><span class="ico"><svg width="22" height="22" viewBox="0 0 22 22"><path d="M3 12 L12 3 L19 3 L19 10 L10 19Z" fill="#222"/><circle cx="15.5" cy="6.5" r="1.6" fill="#fff"/><path d="M8 11 L11 14 M10 9 L13 12" stroke="#fff" stroke-width="1.2"/></svg></span>Coupons</li>
    </ul>
  </div>

  <div class="plan" style="left:794px">
    <div class="plan-head"><b>$4.99</b>subscription</div>
    <ul class="plan-list">
      <li class="plan-item"><span class="ico"><svg width="20" height="24" viewBox="0 0 20 24"><text x="10" y="19" text-anchor="middle" font-family="Roboto,sans-serif" font-size="20" font-weight="500" fill="#222">$</text></svg></span><span>Includes <em>30%</em> off All Products</span></li>
      <li class="plan-item"><span class="ico"><svg width="22" height="16" viewBox="0 0 22 16"><rect width="22" height="16" rx="4" fill="#222"/><path d="M9 4 L15 8 L9 12Z" fill="#fff"/></svg></span>Video Tutorials</li>
      <li class="plan-item"><span class="ico"><svg width="20" height="20" viewBox="0 0 20 20"><rect x="1" y="3" width="18" height="16" rx="2" fill="none" stroke="#222" stroke-width="2"/><path d="M1 8 H19 M6 1 V5 M14 1 V5 M7 8 V19 M13 8 V19 M1 13.5 H19" stroke="#222" stroke-width="1.5"/></svg></span>Weekly Flash Sales</li>
      <li class="plan-item"><span class="ico"><svg width="22" height="22" viewBox="0 0 22 22"><path d="M3 12 L12 3 L19 3 L19 10 L10 19Z" fill="#222"/><circle cx="15.5" cy="6.5" r="1.6" fill="#fff"/><path d="M8 11 L11 14 M10 9 L13 12" stroke="#fff" stroke-width="1.2"/></svg></span>Coupons</li>
    </ul>
  </div>
</section>

<section class="products">
  <h2>OUR PRODUCTS</h2>
  <p class="products-intro">Lorem ipsum dolor sit amet, consectetur adipiscing elit. Nam vestibulum quam viverra arcu ultricies placerat. Fusce volutpat dolor sed odio dignissim facilisis non eu nibh.</p>
  <div class="cat" style="left:77px">
    <div class="cat-photo" style="background:radial-gradient(circle at 40% 45%,#d8b7a8,#5a3a30 70%)" role="img" aria-label="Portrait of a woman with long dark curls"></div>
    <h3>HAIR EXTENSIONS</h3>
    <ul><li>Tapes and Clips</li><li>Weaves</li><li>Wigs</li><li>Tapes</li></ul>
  </div>
  <div class="cat" style="left:297px">
    <div class="cat-photo" style="background:radial-gradient(circle at 45% 45%,#eed9b8,#9a7a58 70%)" role="img" aria-label="Portrait of a blonde woman with wavy hair"></div>
    <h3>HAIR PIECES</h3>
    <ul><li>Ponytails</li><li>Buns</li><li>Braids</li><li>Falls</li></ul>
  </div>
  <div class="cat" style="left:541px">
    <div class="cat-photo" style="background:radial-gradient(circle at 50% 45%,#d9a07c,#6a4030 70%)" role="img" aria-label="Portrait of a woman wearing a turquoise necklace"></div>
    <h3>HAIR ACCESSORIES</h3>
    <ul><li>Headbands</li><li>Hair Ties</li><li>Pins</li><li>Bridal</li></ul>
  </div>
  <div class="cat" style="left:760px">
    <div class="cat-photo" style="background:radial-gradient(circle at 40% 45%,#d8b7a8,#5a3a30 70%)" role="img" aria-label="Portrait of a woman with long dark curls"></div>
    <h3>HAIR CARE</h3>
    <ul><li>Wet Lines</li><li>Dry Lines</li><li>Treatments</li><li>Hair Tools</li></ul>
  </div>
  <div class="cat" style="left:993px">
    <div class="cat-photo" style="background:linear-gradient(110deg,#f5efe8 0,#d9b48a 45%,#a57a52)" role="img" aria-label="Portrait of a woman with long straight blonde hair"></div>
    <h3>SALON BEAUTY</h3>
    <ul><li>Face</li><li>Skin</li><li>Body</li></ul>
  </div>
</section>

<h2 class="section-title" style="left:74px">OUR VIDEO</h2>
<div class="video" role="img" aria-label="Video still of a woman with dark curly hair and a pearl necklace">
  <svg width="56" height="56" viewBox="0 0 56 56"><circle cx="28" cy="28" r="24" fill="none" stroke="rgba(255,255,255,.7)" stroke-width="4"/><path d="M22 17 L39 28 L22 39Z" fill="rgba(255,255,255,.7)"/></svg>
</div>

<h2 class="section-title" style="left:527px">TUTORIALS BLOGS</h2>
<article class="post" style="top:1686px">
  <div class="post-photo" style="background:linear-gradient(120deg,#3a2218,#8a4e32 55%,#c58a64)" role="img" aria-label="Makeup artist applying lipstick to a model"></div>
  <div class="post-body">
    <h4>Nemo Enim Ipsam Volup</h4>
    <time>09-07-2015</time>
    <p>Lorem Ipsum has been the industry's standard dummy text ever since the 1500s, when an unknown printer took a galley of type and scrambled it to make a type specimen book. It has survived not only five centuries,</p>
  </div>
</article>
<article class="post" style="top:1856px">
  <div class="post-photo" style="background:linear-gradient(120deg,#b9c4c8,#8a6a54 55%,#4a3226)" role="img" aria-label="Stylist cutting a client's hair in a salon"></div>
  <div class="post-body">
    <h4>Nemo Enim Ipsam Volup</h4>
    <time>09-07-2015</time>
    <p>Lorem Ipsum has been the industry's standard dummy text ever since the 1500s, when an unknown printer took a galley of type and scrambled it to make a type specimen book. It has survived not only five centuries,</p>
  </div>
</article>

<footer class="footer">
  <div class="foot-brand">VELA GLOW<br>SOCIETY</div>
  <p class="foot-copy">Copyright © 2015. Company Name<br>All Right Reserved</p>
  <ul class="foot-col" style="left:420px"><li>FAQ</li><li>CONTACT US</li><li>CLUB REVIEWS</li></ul>
  <ul class="foot-col" style="left:582px"><li>PRESS</li><li>BLOG</li><li>CAREERS</li></ul>
  <ul class="foot-col" style="left:711px"><li>PRIVACY</li><li>TERMS</li></ul>
  <ul class="foot-col" style="left:834px"><li>PRIVACY</li><li>TERMS</li></ul>
  <div class="social" aria-label="Social links"><span></span><span></span><span></span><span></span><span></span><span></span></div>
</footer>

</body>
</html>
```